brimwood
business cards & stationary
Modern
marcus tolley
director
Brimwood Carpentry Limited
Unit 4 & 6 fenwick trade estate, fenwick, ashcombe, westmoreshire, sk14 7pj
marcus@brimwoodcarpentry.co.uk
www.brimwoodcarpentry.co.uk
I would like the business card to be printed on thick matte black card. I think it would be interesting if the text was printed in silver leaf.
I would like to perhaps see the employee name in all lower case.
Please introduce keywords... architectural joinery ~ bespoke furniture - design somewhere on the card perhaps on back at bottom.
Logo
Web address
Keywords
photo shows a card I like

```html
<!DOCTYPE html>
<html lang="en">
<head>
<meta charset="utf-8">
<title>brimwood — business cards &amp; stationery</title>
<link rel="stylesheet" href="https://fonts.googleapis.com/css2?family=Questrial&display=swap">
<style>
  :root {
    --ink: #0d0d0d;
    --paper: #ffffff;
    --rule: #9a9a9a;
    --window: #eeeeee;
    --window-edge: #c9c9c9;
    --muted: #4a4a4a;
  }
  * { margin: 0; padding: 0; box-sizing: border-box; }
  html, body { width: 1200px; height: 1101px; overflow: hidden; background: var(--paper); }
  body { position: relative; font-family: "Questrial", "Century Gothic", sans-serif; color: var(--ink); }

  .sheet { position: absolute; background: var(--paper); border: 1px solid var(--rule); overflow: hidden; }
  .brand-block { position: absolute; background: var(--ink); color: var(--paper); }
  .brand-name { position: absolute; left: 0; right: 0; text-align: center; letter-spacing: 0.04em; color: var(--paper); }
  .brand-web { position: absolute; left: 0; right: 0; text-align: center; color: var(--paper); }
  .bar { position: absolute; background: var(--ink); }

  /* Letterhead */
  .letterhead { left: 66px; top: 36px; width: 720px; height: 1044px; }
  .letterhead .brand-block { left: 0; top: 0; width: 234px; height: 300px; }
  .letterhead .brand-name { top: 132px; font-size: 40px; }
  .letterhead .brand-web { top: 254px; font-size: 11px; }
  .letterhead .footer-details { position: absolute; left: 84px; top: 954px; width: 600px; font-size: 10.5px; line-height: 1.45; color: var(--muted); white-space: nowrap; }
  .letterhead .bar { left: 0; right: 0; bottom: 6px; height: 24px; }

  /* Business card front */
  .card-front { left: 834px; top: 60px; width: 321px; height: 204px; }
  .card-front .brand-block { left: 0; top: 0; width: 156px; height: 195px; }
  .card-front .brand-name { top: 92px; font-size: 24px; }
  .card-front .holder { position: absolute; left: 171px; top: 20px; }
  .card-front .holder-name { font-size: 12.5px; }
  .card-front .holder-role { font-size: 9px; color: var(--muted); margin-top: 2px; }
  .card-front .contact { position: absolute; left: 171px; top: 86px; width: 144px; font-size: 6.6px; line-height: 1.45; color: var(--muted); white-space: nowrap; }
  .card-front .bar { left: 0; right: 0; bottom: 0; height: 9px; }

  /* Business card back */
  .card-back { left: 834px; top: 294px; width: 321px; height: 171px; background: var(--ink); border-color: var(--ink); }
  .card-back .brand-name { left: 30px; right: auto; top: 62px; font-size: 30px; }
  .card-back .strip { position: absolute; left: 0; right: 0; bottom: 6px; height: 10px; background: var(--paper); }

  /* Envelope */
  .envelope { left: 420px; top: 486px; width: 726px; height: 438px; }
  .envelope .flap { position: absolute; left: 0; top: 0; }
  .envelope .flap-mark { position: absolute; left: 0; right: 0; top: 38px; text-align: center; font-size: 13px; letter-spacing: 0.04em; }
  .envelope .brand-block { left: 0; top: 189px; width: 240px; height: 240px; }
  .envelope .brand-name { top: 92px; font-size: 38px; }
  .envelope .brand-web { top: 198px; font-size: 10px; }
  .envelope .window { position: absolute; left: 255px; top: 189px; width: 360px; height: 180px; background: var(--window); border: 1px solid var(--window-edge); border-radius: 14px; }
  .envelope .return-details { position: absolute; left: 252px; top: 388px; width: 460px; font-size: 6.6px; line-height: 1.45; color: var(--muted); white-space: nowrap; }
  .envelope .bar { left: 240px; right: 0; bottom: 6px; height: 9px; }
</style>
</head>
<body>

<section class="sheet letterhead" aria-label="Letterhead">
  <div class="brand-block">
    <div class="brand-name">brimwood</div>
    <div class="brand-web">www.brimwoodcarpentry.co.uk</div>
  </div>
  <p class="footer-details">
    Adress: Brimwood Carpentry Limited Unit 4 &amp; 6 fenwick trade estate, fenwick<br>
    ashcombe, westmoreshire, sk14 7pj Phone: +44 (0)1632 480112<br>
    Cell: 07700 914226 Email: marcus@brimwoodcarpentry.co.uk
  </p>
  <div class="bar"></div>
</section>

<section class="sheet card-front" aria-label="Business card front">
  <div class="brand-block">
    <div class="brand-name">brimwood</div>
  </div>
  <div class="holder">
    <div class="holder-name">marcus tolley</div>
    <div class="holder-role">Director</div>
  </div>
  <p class="contact">
    Adress:<br>
    Brimwood Carpentry Limited<br>
    Unit 4 &amp; 6 fenwick trade estate<br>
    fenwick, ashcombe,<br>
    westmoreshire, sk14 7pj<br>
    Phone: +44 (0)1632 480112<br>
    Cell: 07700 914226<br>
    Email: marcus@brimwoodcarpentry.co.uk
  </p>
  <div class="bar"></div>
</section>

<section class="sheet card-back" aria-label="Business card back">
  <div class="brand-name">brimwood</div>
  <div class="strip"></div>
</section>

<section class="sheet envelope" aria-label="Envelope">
  <svg class="flap" width="726" height="438" viewBox="0 0 726 438" aria-hidden="true">
    <polyline points="0,0 363,150 726,0" fill="none" stroke="#d6d6d6" stroke-width="1"/>
  </svg>
  <div class="flap-mark">brimwood</div>
  <div class="brand-block">
    <div class="brand-name">brimwood</div>
    <div class="brand-web">www.brimwoodcarpentry.co.uk</div>
  </div>
  <div class="window"></div>
  <p class="return-details">
    Adress: Brimwood Carpentry Limited Unit 4 &amp; 6 fenwick trade estate, fenwick, ashcombe, westmoreshire, sk14 7pj<br>
    Phone: +44 (0)1632 480112 Cell: 07700 914226 Email: marcus@brimwoodcarpentry.co.uk
  </p>
  <div class="bar"></div>
</section>

</body>
</html>
```